SEO AND WEB DESIGN COMPANY BUSINESS CARD DESIGN

I need an eye catching , simple business card design that will match my logo . I need 2 versions of it ( white background and black background) - SOME PEOPLE DID NOT GET IT AND SENDING US FRONT WHITE BACK WHITE VERSIONS WHICH IS NOT CORRECT.

ONE VERSION SHOULD BE BACK AND FRONT ALL BLACK , SECOND VERSION SHOULD BE BACK AND FRONT ALL WHITE

logo psd files are attached for both versions. The business card is going to have : First Name- Last name - position - phone numbers

```html
<!DOCTYPE html>
<html lang="en">
<head>
<meta charset="utf-8">
<title>Ridgeway Studio – Business Card, Black Version</title>
<link href="https://fonts.googleapis.com/css2?family=Lato:wght@400;700&display=swap" rel="stylesheet">
<style>
  :root {
    --backdrop: #141415;
    --card: #1e1f21;
    --ink-white: #f2f2f2;
    --ink-grey: #8d8f93;
    --accent-blue: #3b8fe6;
  }
  html, body {
    margin: 0;
    padding: 0;
    width: 1200px;
    height: 912px;
    overflow: hidden;
    background: var(--backdrop);
    font-family: "Lato", Arial, sans-serif;
  }
  .canvas {
    position: relative;
    width: 1200px;
    height: 912px;
    display: flex;
    flex-direction: column;
    align-items: center;
    justify-content: center;
    gap: 40px;
  }
  .card {
    position: relative;
    width: 700px;
    height: 400px;
    background: var(--card);
    box-sizing: border-box;
  }

  /* Front side */
  .card--front {
    display: flex;
    align-items: center;
    justify-content: center;
  }
  .brand {
    display: flex;
    align-items: center;
    gap: 14px;
  }
  .brand__dot {
    width: 26px;
    height: 26px;
    border-radius: 50%;
    background: var(--ink-grey);
  }
  .brand__name {
    font-weight: 700;
    font-size: 52px;
    letter-spacing: 1px;
    text-transform: uppercase;
    color: var(--ink-grey);
  }

  /* Back side */
  .card--back {
    display: flex;
    align-items: center;
    padding-left: 70px;
  }
  .card--back .brand__dot {
    width: 20px;
    height: 20px;
    background: var(--accent-blue);
  }
  .card--back .brand__name {
    font-size: 34px;
    color: var(--ink-white);
  }
  .divider {
    width: 2px;
    height: 110px;
    background: var(--accent-blue);
    margin: 0 34px;
  }
  .contact__name {
    font-weight: 700;
    font-size: 24px;
    text-transform: uppercase;
    color: var(--accent-blue);
    letter-spacing: 0.3px;
  }
  .contact__role {
    font-size: 18px;
    color: var(--ink-white);
    margin-top: 4px;
  }
  .contact__phone {
    display: flex;
    align-items: center;
    gap: 10px;
    margin-top: 14px;
    font-size: 19px;
    color: var(--ink-white);
  }
  .contact__phone svg {
    width: 16px;
    height: 16px;
    fill: var(--accent-blue);
  }
</style>
</head>
<body>
<main class="canvas">
  <section class="card card--front" aria-label="Card front">
    <div class="brand">
      <span class="brand__dot"></span>
      <span class="brand__name">Ridgeway Studio</span>
    </div>
  </section>

  <section class="card card--back" aria-label="Card back">
    <div class="brand">
      <span class="brand__dot"></span>
      <span class="brand__name">Ridgeway Studio</span>
    </div>
    <div class="divider"></div>
    <div class="contact">
      <div class="contact__name">Calvin Hartley</div>
      <div class="contact__role">Manager</div>
      <div class="contact__phone">
        <svg viewBox="0 0 24 24" aria-hidden="true"><path d="M6.6 10.8a15.1 15.1 0 0 0 6.6 6.6l2.2-2.2a1 1 0 0 1 1-.25 11.4 11.4 0 0 0 3.6.57 1 1 0 0 1 1 1V20a1 1 0 0 1-1 1A17 17 0 0 1 3 4a1 1 0 0 1 1-1h3.5a1 1 0 0 1 1 1c0 1.25.2 2.45.57 3.57a1 1 0 0 1-.25 1z"/></svg>
        <span>555 014 2290</span>
      </div>
    </div>
  </section>
</main>
</body>
</html>
```